Health and wellnes company needs business cards

We are a Health and wellness business just relocated to Spain. Here nobody knows our business so we would like to put some of our services on the card. Clean design with logo.

Contact Information for Business Card

Brightmeadow
Clara & Tobias Wennberg
Calle de los Almendros 17
Villanueva del Prado
Mobile: 0046 731 402768
info@brightmeadow-example.se

Font styles to use
Serif

Colors
85cae6
85acd3
b768aa

Requirements
Must have
• these Services somewhere on the card
• - Private or group yoga
• - Reconnective healing
• - Kitesurfing lessons
• - Massage
• LOgo somewhere
Nice to have
• Colours that go with the logo please

```html
<!DOCTYPE html>
<html lang="en">
<head>
<meta charset="utf-8">
<title>Brightmeadow business card</title>
<link href="https://fonts.googleapis.com/css2?family=Lato:wght@400;700&family=Marcellus&display=swap" rel="stylesheet">
<style>
  :root {
    --navy: #1f3a6b;
    --navy-deep: #1a3260;
    --teal: #5bc0c6;
    --ink: #333a44;
    --paper: #ffffff;
    --backdrop: #e9ebef;
  }
  * { margin: 0; padding: 0; box-sizing: border-box; }
  html, body { width: 1200px; height: 900px; overflow: hidden; }
  body {
    background: var(--backdrop);
    display: flex;
    align-items: center;
    justify-content: center;
    gap: 40px;
    font-family: "Lato", sans-serif;
  }
  .card {
    width: 540px;
    height: 320px;
    border-radius: 22px;
    position: relative;
    overflow: hidden;
    box-shadow: 0 6px 18px rgba(0,0,0,0.12);
  }

  /* Front */
  .card-front { background: var(--paper); }
  .brand {
    position: absolute;
    left: 38px;
    top: 34px;
    display: flex;
    align-items: center;
    gap: 14px;
  }
  .brand-dot {
    width: 46px; height: 46px;
    border-radius: 50%;
    border: 5px solid var(--teal);
  }
  .brand-name {
    font-family: "Marcellus", serif;
    font-size: 30px;
    letter-spacing: 1px;
    color: var(--navy);
    text-transform: uppercase;
  }
  .front-rule {
    position: absolute;
    left: 38px; right: 38px;
    top: 106px;
    height: 1.5px;
    background: var(--navy);
  }
  .contact {
    position: absolute;
    left: 38px;
    top: 122px;
    font-size: 14px;
    line-height: 1.55;
    color: var(--ink);
    list-style: none;
  }
  .contact li { display: flex; align-items: center; gap: 8px; }
  .contact .indent { padding-left: 22px; }
  .contact svg { width: 14px; height: 14px; fill: var(--navy); flex: none; }
  .owners {
    position: absolute;
    right: 38px;
    bottom: 46px;
    font-weight: 700;
    font-size: 22px;
    color: var(--navy);
  }
  .owners-rule {
    position: absolute;
    right: 38px;
    width: 300px;
    bottom: 34px;
    height: 1.5px;
    background: var(--navy);
  }

  /* Back */
  .card-back { background: var(--navy); display: flex; }
  .services {
    flex: 1;
    padding: 52px 0 0 44px;
    list-style: none;
  }
  .services li {
    display: flex;
    align-items: center;
    gap: 16px;
    color: #ffffff;
    font-size: 21px;
    margin-bottom: 16px;
  }
  .service-icon {
    width: 26px; height: 26px;
    border-radius: 4px;
    background: var(--teal);
    flex: none;
  }
  .back-band {
    width: 92px;
    background: var(--paper);
    display: flex;
    align-items: center;
    justify-content: center;
  }
  .back-band span {
    font-family: "Marcellus", serif;
    font-size: 32px;
    letter-spacing: 1px;
    color: var(--navy-deep);
    text-transform: uppercase;
    transform: rotate(-90deg);
    white-space: nowrap;
  }
</style>
</head>
<body>
  <section class="card card-front">
    <div class="brand">
      <div class="brand-dot"></div>
      <div class="brand-name">Brightmeadow</div>
    </div>
    <div class="front-rule"></div>
    <ul class="contact">
      <li class="indent">Calle de los Almendros 17</li>
      <li class="indent">Villanueva del Prado</li>
      <li>
        <svg viewBox="0 0 24 24" aria-hidden="true"><path d="M6.6 10.8a15 15 0 0 0 6.6 6.6l2.2-2.2a1 1 0 0 1 1-.25 11.4 11.4 0 0 0 3.6.57 1 1 0 0 1 1 1V20a1 1 0 0 1-1 1A17 17 0 0 1 3 4a1 1 0 0 1 1-1h3.5a1 1 0 0 1 1 1c0 1.25.2 2.45.57 3.57a1 1 0 0 1-.25 1z"/></svg>
        0046 731 402768
      </li>
      <li>
        <svg viewBox="0 0 24 24" aria-hidden="true"><path d="M2 5h20v14H2z M2 5l10 8 10-8" fill="none" stroke="#1f3a6b" stroke-width="2"/></svg>
        info@brightmeadow-example.se
      </li>
    </ul>
    <div class="owners">Clara &amp; Tobias Wennberg</div>
    <div class="owners-rule"></div>
  </section>

  <section class="card card-back">
    <ul class="services">
      <li><span class="service-icon" role="img" aria-label="Yoga pose icon"></span>Private or group yoga</li>
      <li><span class="service-icon" role="img" aria-label="Healing hands icon"></span>Reconnective healing</li>
      <li><span class="service-icon" role="img" aria-label="Kitesurfer icon"></span>Kitesurfing lessons</li>
      <li><span class="service-icon" role="img" aria-label="Massage icon"></span>Massage</li>
    </ul>
    <div class="back-band"><span>Brightmeadow</span></div>
  </section>
</body>
</html>
```